Business cards for law firm with global theme

I'd like business cards with contact info for two offices. They should include the colors and font of the new logo design, which is a stylized globe with an "F" in it. The feel should be very modern and professional.

```html
<!DOCTYPE html>
<html lang="en">
<head>
<meta charset="utf-8">
<title>Veranti Law — Business Cards</title>
<link rel="stylesheet" href="https://fonts.googleapis.com/css2?family=Cinzel:wght@500&display=swap">
<style>
  :root {
    --backdrop: #0a7391;
    --card-blue: #11a9ef;
    --navy: #0c3873;
    --slate: #54739c;
    --white: #ffffff;
    --type: "Cinzel", serif;
  }
  * { margin: 0; padding: 0; box-sizing: border-box; }
  html, body { width: 1200px; height: 982px; overflow: hidden; }
  body { background: var(--backdrop); font-family: var(--type); color: var(--white); }

  .canvas { position: relative; width: 1200px; height: 982px; }

  .card {
    position: absolute;
    width: 369px;
    height: 588px;
    background: var(--card-blue);
    overflow: hidden;
    box-shadow: 0 6px 18px rgba(0, 40, 60, 0.35);
  }
  .card--front { left: 215px; top: 156px; }
  .card--back  { left: 619px; top: 154px; }

  .card__arc { position: absolute; inset: 0; width: 100%; height: 100%; }

  /* Wordmark: laid out horizontally, then turned to read bottom-to-top */
  .wordmark {
    position: absolute;
    display: flex;
    flex-direction: column;
    align-items: stretch;
    transform: rotate(-90deg);
    font-weight: 500;
    line-height: 1;
  }
  .wordmark__name { text-align: center; letter-spacing: 0.02em; }
  .wordmark__sub {
    display: flex;
    align-items: center;
    gap: 6px;
    letter-spacing: 0.08em;
  }
  .wordmark__sub::before,
  .wordmark__sub::after { content: ""; flex: 1; height: 1.5px; background: var(--white); }

  .card--front .wordmark { left: 118px; top: 136px; width: 238px; height: 62px; }
  .card--front .wordmark__name { font-size: 38px; }
  .card--front .wordmark__sub { font-size: 22px; margin-top: 2px; }

  .card--back .wordmark { left: -5px; top: 409px; width: 130px; height: 34px; }
  .card--back .wordmark__name { font-size: 21px; }
  .card--back .wordmark__sub { font-size: 12px; gap: 4px; }

  .brand-dot {
    position: absolute;
    border-radius: 50%;
    background: var(--white);
  }
  .card--front .brand-dot { left: 98px; top: 119px; width: 93px; height: 93px; }
  .card--back .brand-dot  { left: 30px; top: 505px; width: 53px; height: 53px; }

  /* Contact column */
  .contact__line {
    position: absolute;
    bottom: 83px;
    writing-mode: vertical-rl;
    transform: rotate(180deg);
    font-size: 11.5px;
    font-weight: 500;
    letter-spacing: 0.03em;
    white-space: nowrap;
  }
  .contact__icon {
    position: absolute;
    top: 529px;
    width: 22px;
    height: 22px;
  }
</style>
</head>
<body>
<main class="canvas">

  <section class="card card--front" aria-label="Card front">
    <svg class="card__arc" viewBox="0 0 369 588" aria-hidden="true">
      <circle cx="184" cy="602" r="266" fill="var(--white)"/>
      <circle cx="184" cy="602" r="235" fill="var(--navy)"/>
      <circle cx="184" cy="602" r="195" fill="var(--slate)"/>
    </svg>
    <span class="brand-dot" aria-hidden="true"></span>
    <div class="wordmark">
      <span class="wordmark__name">VERANTI</span>
      <span class="wordmark__sub">LAW</span>
    </div>
  </section>

  <section class="card card--back" aria-label="Card back">
    <svg class="card__arc" viewBox="0 0 369 588" aria-hidden="true">
      <circle cx="184" cy="1" r="266" fill="var(--white)"/>
      <circle cx="184" cy="1" r="235" fill="var(--navy)"/>
      <circle cx="184" cy="1" r="195" fill="var(--slate)"/>
    </svg>

    <span class="brand-dot" aria-hidden="true"></span>
    <div class="wordmark">
      <span class="wordmark__name">VERANTI</span>
      <span class="wordmark__sub">LAW</span>
    </div>

    <ul class="contact" style="list-style:none">
      <li><span class="contact__line" style="left:154px">Your Number</span></li>
      <li><span class="contact__line" style="left:190px">Your Number</span></li>
      <li><span class="contact__line" style="left:219px">Your Email</span></li>
      <li><span class="contact__line" style="left:254px">Your Website</span></li>
      <li><span class="contact__line" style="left:292px">Your Address</span></li>
    </ul>

    <svg class="contact__icon" style="left:152px" viewBox="0 0 24 24" aria-label="Phone">
      <path d="M16 3l4 2-3 7c-2 5-6 8-11 9l-3-3 4-3 2 2c2-1 4-3 5-6l-2-1z" fill="var(--white)"/>
    </svg>
    <svg class="contact__icon" style="left:186px" viewBox="0 0 24 24" aria-label="Phone">
      <path d="M16 3l4 2-3 7c-2 5-6 8-11 9l-3-3 4-3 2 2c2-1 4-3 5-6l-2-1z" fill="var(--white)"/>
    </svg>
    <svg class="contact__icon" style="left:218px" viewBox="0 0 24 24" aria-label="Email">
      <rect x="4" y="2" width="16" height="20" rx="1.5" fill="var(--white)"/>
      <path d="M7 4l8 8-8 8" fill="none" stroke="var(--card-blue)" stroke-width="1.6"/>
    </svg>
    <svg class="contact__icon" style="left:251px" viewBox="0 0 24 24" aria-label="Website">
      <circle cx="12" cy="12" r="10" fill="var(--white)"/>
      <path d="M2 12h20M12 2v20M4 7h16M4 17h16" stroke="var(--card-blue)" stroke-width="1.4" fill="none"/>
      <ellipse cx="12" cy="12" rx="4.5" ry="10" fill="none" stroke="var(--card-blue)" stroke-width="1.4"/>
    </svg>
    <svg class="contact__icon" style="left:288px" viewBox="0 0 24 24" aria-label="Address">
      <path d="M2 12c4-6 12-8 20 0-8 8-16 6-20 0z" fill="var(--white)"/>
      <circle cx="11" cy="12" r="2.6" fill="var(--card-blue)"/>
    </svg>
  </section>

</main>
</body>
</html>
```